Travel Blogger Business Card for roamquill.net

I need a two-sided business card for a travel blogging website. The card should be both professional and fun at the same time. This is for the website www.roamquill.net

I don't necessarily think that the current logo on the website needs to be used on the business card but it can be. I am very flexible with ideas

Target Market(s)

Travel agencies that will be met at a conference.

Industry/Entity Type

Travel

Contact Information for Business Card

Company Name: Roam Quill.net
Name: Bertrand Olesky
Voice: +1-(345)-402-7731
Address: Coral Reach Shore, Grand Cayman, Cayman Islands
Email: ceo@roamquill.net

Colors
0592cd
0355a3
3176b5
33a6d7
85cae6
85acd3

Requirements
Must have
• Website address and name should be bigger than address, phone number, and email.

```html
<!DOCTYPE html>
<html lang="en">
<head>
<meta charset="utf-8">
<title>Roam Quill.net – Business Card</title>
<link rel="stylesheet" href="https://fonts.googleapis.com/css2?family=Fira+Sans:wght@300;400;600&display=swap">
<style>
  :root {
    --card-bg: #1f1f21;
    --brand-blue: #0592cd;
    --blue-deep: #0355a3;
    --blue-mid: #3176b5;
    --blue-bright: #33a6d7;
    --blue-light: #85cae6;
    --blue-pale: #85acd3;
    --text-light: #ffffff;
  }
  html, body {
    margin: 0;
    padding: 0;
    width: 1200px;
    height: 667px;
    overflow: hidden;
    background: var(--card-bg);
  }
  .card {
    position: relative;
    width: 1200px;
    height: 667px;
    background: var(--card-bg);
    font-family: "Fira Sans", "Source Sans 3", sans-serif;
    color: var(--text-light);
  }
  .card-art {
    position: absolute;
    inset: 0;
  }
  .brand-name {
    position: absolute;
    top: 136px;
    left: 0;
    width: 100%;
    text-align: center;
    margin: 0;
    font-size: 40px;
    line-height: 50px;
    font-weight: 600;
    color: var(--brand-blue);
  }
  .holder-name {
    position: absolute;
    top: 301px;
    left: 0;
    width: 100%;
    text-align: center;
    margin: 0;
    font-size: 44px;
    font-weight: 300;
    line-height: 60px;
  }
  .contact {
    position: absolute;
    margin: 0;
    font-weight: 400;
    font-style: normal;
  }
  .contact-address {
    left: 28px;
    top: 570px;
    font-size: 26px;
    line-height: 33px;
  }
  .contact-phone {
    left: 466px;
    top: 567px;
    font-size: 31px;
    line-height: 36px;
  }
  .contact-email {
    left: 786px;
    top: 567px;
    font-size: 32px;
    line-height: 36px;
  }
</style>
</head>
<body>
<main class="card">
  <svg class="card-art" width="1200" height="667" viewBox="0 0 1200 667" aria-hidden="true">
    <circle class="brand-dot" cx="600" cy="72" r="38" fill="var(--brand-blue)"/>

    <rect class="name-band" x="0" y="300" width="1200" height="67" fill="var(--brand-blue)"/>
    <polygon class="band-stripe" points="0,305 0,336 490,367" fill="var(--blue-bright)"/>
    <polygon class="band-stripe" points="0,336 0,367 490,367" fill="var(--blue-light)"/>
    <polygon class="band-stripe" points="1200,305 1200,336 710,367" fill="var(--blue-bright)"/>
    <polygon class="band-stripe" points="1200,336 1200,367 710,367" fill="var(--blue-light)"/>

    <polygon class="name-plate" points="526,202 674,202 713,334 674,466 526,466 487,334" fill="var(--brand-blue)"/>
    <polygon class="plate-tab" points="526,202 674,202 655,246 545,246" fill="var(--blue-mid)"/>
    <polygon class="plate-tab" points="545,421 655,421 674,466 526,466" fill="var(--blue-mid)"/>

    <g class="icon icon-pin">
      <circle cx="184" cy="510" r="28" fill="var(--brand-blue)"/>
      <path d="M184 493 a11 11 0 0 1 11 11 c0 8 -11 20 -11 20 s-11 -12 -11 -20 a11 11 0 0 1 11 -11z" fill="var(--text-light)"/>
      <circle cx="184" cy="504" r="4" fill="var(--brand-blue)"/>
    </g>
    <g class="icon icon-phone">
      <circle cx="595" cy="510" r="28" fill="var(--brand-blue)"/>
      <path d="M583 496 l6 -2 l5 10 l-4 4 c2 5 6 9 11 11 l4 -4 l10 5 l-2 6 c-2 3 -6 4 -9 3 c-11 -4 -19 -12 -23 -23 c-1 -3 0 -7 2 -10z" fill="var(--text-light)"/>
    </g>
    <g class="icon icon-mail">
      <circle cx="927" cy="510" r="28" fill="var(--brand-blue)"/>
      <rect x="911" y="499" width="32" height="22" rx="2" fill="var(--text-light)"/>
      <polyline points="911,500 927,512 943,500" fill="none" stroke="var(--brand-blue)" stroke-width="2.5"/>
    </g>

    <g class="divider">
      <line x1="456" y1="539" x2="456" y2="651" stroke="var(--blue-pale)" stroke-width="2.5"/>
      <circle cx="456" cy="539" r="4.5" fill="var(--brand-blue)"/>
      <circle cx="456" cy="651" r="4.5" fill="var(--brand-blue)"/>
    </g>
    <g class="divider">
      <line x1="743" y1="539" x2="743" y2="651" stroke="var(--blue-pale)" stroke-width="2.5"/>
      <circle cx="743" cy="539" r="4.5" fill="var(--brand-blue)"/>
      <circle cx="743" cy="651" r="4.5" fill="var(--brand-blue)"/>
    </g>
  </svg>

  <p class="brand-name">Roam Quill.net</p>
  <h1 class="holder-name">Bertrand Olesky</h1>

  <address class="contact contact-address">Coral Reach Shore, Grand Cayman<br>Cayman Islands</address>
  <p class="contact contact-phone">+1-(345)-402-7731</p>
  <p class="contact contact-email">ceo@roamquill.net</p>
</main>
</body>
</html>
```